Dust N Gone! Cleaning needs a flyer!

We have started a cleaning business DUST N GONE! Cleaning, and had a new logo design for it.
We would like a flyer designed to present to businesses that represents our professionalism, quality of service, security and value for money.
We would like a flyer that we can present to both our residential clients and business owners alike.
We will use this flyer for the next 2 years without having to make changes.
I'm happy for the designer to come up with their own wording if necessary.
Updates

Hello everyone!

In addition to the information I have already provided, please see below for more information to be included on the design for our flyer.

Thank you in advance.

Don’t read this unless your current cleaners are AMAZING!

Are you still reading? Now for the good news! Announcing the arrival of the amazing cleaning team of Dust N Gone! Cleaning. They’re the BEST in the Wimmera and we personally guarantee it.

We offer an ultimate service that NO other cleaning company in the Wimmera can offer; high quality cleaning of your home or business, carpet dry cleaning and pest control. All of these services can be completed at a time that is most convenient to you.

From wiping benches to washing windows, from dusting skirting boards to dry cleaning your carpets, from bathrooms to bugs, we really are your ONE stop shop.

Why choose the greatest cleaning company in the Wimmera?

For over 18 years, we have built a reputation on honesty and trust in the residential and commercial services. Our business is to know what people expect when we walk in to your home or business.

With our vast experience and knowledge, we know how to find the best people for the job, how to identify the best products for the clean, we use the newest of technology and equipment and have the best attitudes in town.

Local people, local business that you can rely on because we are also Dust N Gone! Pest Control & Fibrela all rolled in to your ONE stop shop for residential services.

Call us to discuss how we can give you the quality you demand.

Residential Cleaning                                                       Commercial Cleaning                                     

General house cleaning                                                  Business Premises          

Home help                                                                         Vacated properties

Rental vacancies                                                               Schools

Post renovation cleans                                                     Motels/Hotels

 

                                   

Target Market(s)

Business owners, commercial properties, home owners (women aged between 30 - 80y/o)

Industry/Entity Type

Residential

Requirements
Must have
• Incorporate our logo and colours.
Double sided.
Images of interiors of both home & office.
Catch phrase: "You demand quality ..... we guarantee it!"
Address: 22-26 Wattlegum St, Horsham VIC 3400
Phone: 1300 482 316
ABN: 47 308 562 194
We complete the ususal cleaning such as:
General House cleaning
Commercial Cleaning
Rental Properties
Business Premises
Other services we offer is:
Carpet dry cleaning
Upholstery cleaning
Dust N Gone! Mite Chasers pest control
Window cleaning.

```html
<!DOCTYPE html>
<html lang="en">
<head>
<meta charset="utf-8">
<title>Dust N Gone! Cleaning – Flyer</title>
<link rel="stylesheet" href="https://fonts.googleapis.com/css2?family=Questrial&family=Andika&family=Archivo+Narrow:wght@400;700&display=swap">
<style>
  :root {
    --ink: #222023;
    --sky-top: #7f9fc4;
    --sky-low: #d9e2ea;
    --magenta: #ec1ee0;
    --gold: #f6c300;
    --paper: #ffffff;
  }
  * { margin: 0; padding: 0; box-sizing: border-box; }
  html, body { width: 848px; height: 1200px; overflow: hidden; background: var(--ink); }
  .flyer { position: relative; width: 848px; height: 1200px; overflow: hidden; background: var(--ink); font-family: "Archivo Narrow", "Arial Narrow", sans-serif; color: var(--paper); }
  .sky { position: absolute; inset: 0 0 auto 0; height: 300px; background: linear-gradient(180deg, var(--sky-top) 0%, #a9bfd6 45%, var(--sky-low) 100%); }
  .house { position: absolute; left: 0; top: 0; }
  .brand { position: absolute; left: 113px; top: 262px; width: 400px; text-align: center; font-family: "Questrial", sans-serif; font-weight: 400; color: var(--paper); }
  .brand-name { display: block; font-size: 57px; line-height: 1; letter-spacing: 0; white-space: nowrap; }
  .brand-sub { display: block; margin-top: 44px; font-size: 28px; letter-spacing: 33px; padding-left: 33px; line-height: 1; white-space: nowrap; }
  .frame { position: absolute; left: 42px; top: 388px; width: 756px; height: 766px; border: 4px solid var(--gold); border-top: none; }
  .catchphrase { position: absolute; left: 70px; width: 708px; top: 423px; text-align: center; font-family: "Andika", sans-serif; font-variant: small-caps; font-size: 28px; color: var(--gold); letter-spacing: 0; white-space: nowrap; }
  .headline { position: absolute; left: 70px; top: 476px; font-size: 28.5px; font-weight: 400; color: var(--magenta); white-space: nowrap; letter-spacing: -0.2px; }
  .headline strong { color: var(--paper); font-weight: 700; }
  .copy { position: absolute; left: 70px; width: 492px; font-size: 14.6px; line-height: 23.6px; }
  .copy-intro { top: 536px; }
  .copy-why { top: 877px; }
  .subhead { position: absolute; left: 70px; top: 780px; line-height: 1; font-weight: 400; }
  .subhead-top { display: block; font-size: 25px; color: var(--magenta); }
  .subhead-main { display: block; font-size: 31px; color: var(--gold); margin-top: 2px; }
  .subhead-main span { color: var(--paper); }
  .photo { position: absolute; left: 567px; width: 225px; }
  .photo-bedroom { top: 537px; height: 175px; background: linear-gradient(160deg, #f3efe9, #d8cdbf 70%, #b79b7c); }
  .photo-office { top: 747px; height: 168px; background: linear-gradient(170deg, #d9e3cf, #9dbe30 35%, #8b8d91 70%, #6a5a4a); }
  .photo-lounge { top: 948px; height: 172px; background: linear-gradient(170deg, #e8d8bd, #c39a6b 55%, #6e6aa8 85%, #4a3a30); }
</style>
</head>
<body>
<main class="flyer">
  <div class="sky" role="img" aria-label="Soft blue sky with light clouds"></div>

  <svg class="house" width="848" height="1200" viewBox="0 0 848 1200" aria-hidden="true">
    <polygon points="0,282 245,8 328,96 328,42 358,42 358,130 840,292 848,292 848,1200 0,1200" fill="#222023"/>
    <polygon points="0,262 245,-2 318,76 318,36 368,36 368,118 848,286 848,298 838,298 350,136 348,58 338,58 338,114 245,24 0,296" fill="#ec1ee0"/>
  </svg>

  <div class="brand">
    <span class="brand-name">DUST N GONE!</span>
    <span class="brand-sub">CLEANING</span>
  </div>

  <div class="frame"></div>

  <p class="catchphrase">"You demand quality ..... we guarantee it!"</p>
  <h1 class="headline">Don’t read this unless your current cleaners are <strong>AMAZING!</strong></h1>

  <div class="copy copy-intro">
    <p>Are you still reading? Now for the good news! Announcing the arrival of the amazing cleaning team of Dust N Gone! Cleaning. They’re the BEST in the Wimmera and we personally guarantee it.</p>
    <p>We offer an ultimate service that NO other cleaning company in the Wimmera can offer; high quality cleaning of your home or business, carpet dry cleaning and pest control. All of these services can be completed at a time that is most convenient to you.</p>
    <p>From wiping benches to washing windows, from dusting skirting boards to dry cleaning your carpets, from bathrooms to bugs, we really are your ONE stop shop.</p>
  </div>

  <h2 class="subhead">
    <span class="subhead-top">Why choose the greatest</span>
    <span class="subhead-main">cleaning company in <span>the Wimmera?</span></span>
  </h2>

  <div class="copy copy-why">
    <p>For over 18 years, we have built a reputation on honesty and trust in the residential and commercial services. Our business is to know what people expect when we walk in to your home or business.</p>
    <p>With our vast experience and knowledge, we know how to find the best people for the job, how to identify the best products for the clean, we use the newest of technology and equipment and have the best attitudes in town.</p>
    <p>Local people, local business that you can rely on because we are also Dust N Gone! Pest Control &amp; Fibrela all rolled in to your ONE stop shop for residential services.</p>
  </div>

  <div class="photo photo-bedroom" role="img" aria-label="Bright, tidy white bedroom interior"></div>
  <div class="photo photo-office" role="img" aria-label="Clean home office with green feature wall"></div>
  <div class="photo photo-lounge" role="img" aria-label="Warm living room with sofas and chandelier"></div>
</main>
</body>
</html>
```